Last Minute Accommodation Booking Portal

AlpenGlowDeals.com needs a web platform to put potential clients in touch with available local ski resort accommodation. We are a dynamic, friendly and versatile company; we like a clean, graphic, contemporary look!

Hotel and apartment owners offer rooms to rent for certain dates with pricing; clients can ask for specific dates and number of beds with their budget. Offers can see searchers requests, searchers can only see offers.

All dates requested and offered must be within two weeks of the posting date and then posts should be removed when their arrival date has passed or they can be deleted by the person posting. We are envisaging that the hotels/apartments and customers would each need to register and login their offer/request.

Target Market(s)

28-55 years, active, high net worth but like a bargain, last mintue deciders, skiers and snowboarders or mountain enthusiasts, city folk wanting a winter break

Industry/Entity Type

Accommodation

Coding

Number of Pages Required

Font styles to use
Sans Serif

Colors
cee9f5
33a6d7
e34297
b768aa
ffffff

Requirements
Must have
• Efficient functionality so that many different parties - both offering deals and searching for deals - can search/list at the same time.
• option to translate to french
Nice to have
• opt in to 'alert/notification' when new offer or search is listed

```html
<!DOCTYPE html>
<html lang="en">
<head>
<meta charset="utf-8">
<title>AlpenGlowDeals.com</title>
<link href="https://fonts.googleapis.com/css2?family=Open+Sans:wght@400;600;700&display=swap" rel="stylesheet">
<style>
:root{
  --brand:#2c6cc4;
  --brand-dark:#1f58a8;
  --btn:#3478d1;
  --accent:#e34297;
  --sky:#cee9f5;
  --page:#ececec;
  --white:#ffffff;
  --text:#444444;
  --muted:#777777;
  --footer:#1f1f1f;
  --footer-bar:#141414;
  --line:#dddddd;
}
*{box-sizing:border-box;margin:0;padding:0}
html,body{width:1200px;height:2228px;overflow:hidden}
body{font-family:"Open Sans",Arial,sans-serif;background:var(--page);color:var(--text);position:relative}

.site-header{position:absolute;top:0;left:0;width:1200px;height:108px;background:var(--brand)}
.logo{position:absolute;left:142px;top:14px;color:var(--white);font-size:30px;font-weight:400;letter-spacing:.5px}
.account-links{position:absolute;right:142px;top:24px;display:flex;gap:26px;font-size:13px;color:#dbe8fa}
.main-nav{position:absolute;left:142px;right:142px;top:74px;display:flex;justify-content:space-between;font-size:14px;color:var(--white);font-weight:600}

.hero{position:absolute;top:108px;left:0;width:1200px;height:520px;background:linear-gradient(180deg,#4a78b8 0%,#8fb3d9 35%,#dfe9f2 60%,#c9d4de 80%,#9aa6b2 100%)}
.hero-arrow{position:absolute;top:256px;width:28px;height:28px;border-radius:50%;background:var(--white)}
.hero-arrow.prev{left:6px}.hero-arrow.next{right:6px}
.hero-arrow svg{display:block}

.search-panel{position:absolute;left:152px;top:472px;width:900px;height:150px;background:var(--brand);padding:28px 36px}
.search-row{display:flex;gap:36px;margin-bottom:22px}
.field{height:32px;background:var(--white);font-size:12px;color:var(--muted);padding:8px 12px;position:relative;width:206px}
.field.wide{width:206px}
.field .caret{position:absolute;right:10px;top:13px;width:0;height:0;border-left:4px solid transparent;border-right:4px solid transparent;border-top:5px solid #888}
.search-btn{width:206px;height:32px;background:var(--btn);color:var(--white);font-size:12px;font-weight:700;text-align:center;line-height:32px;border:1px solid #5a93e0}

.section{position:absolute;left:152px;width:900px;background:var(--white)}
.section-title{font-size:26px;color:var(--brand);font-weight:400;padding:20px 0 0 0}
.recent{top:640px;height:412px;padding:0 0 0 0}
.recent .section-title{padding-left:8px}
.destinations{top:1488px;height:402px}
.destinations .section-title{padding-left:8px}

.card-row{position:absolute;left:0;right:0;top:72px;display:flex;justify-content:space-around;padding:0 10px}
.card{width:268px}
.card-photo{height:148px;width:268px}
.card-name{font-size:12px;color:#d9343a;margin-top:8px}
.card-price{font-size:11px;color:var(--muted);margin-top:6px}
.card-actions{display:flex;align-items:center;justify-content:space-between;margin-top:10px;padding-right:8px}
.details-btn{display:flex;align-items:center;gap:10px;background:var(--btn);color:var(--white);font-size:11px;font-weight:700;height:30px;padding:0 10px}
.card hr{border:0;border-top:1px solid var(--line);margin-top:10px}

.luxury{top:1080px;height:384px}
.family-photo{position:absolute;left:20px;top:22px;width:300px;height:340px;background:linear-gradient(180deg,#f6f6f6,#e9e4e2)}
.luxury-title{position:absolute;left:372px;top:132px;font-size:24px;color:var(--text)}
.thumb-grid{position:absolute;left:372px;top:192px;display:grid;grid-template-columns:repeat(4,120px);gap:12px 14px}
.thumb{height:70px;position:relative}
.thumb-label{position:absolute;left:8px;top:8px;color:var(--white);font-size:9px;font-weight:700}

.site-footer{position:absolute;top:1920px;left:0;width:1200px;height:260px;background:var(--footer);color:#bbbbbb}
.footer-cols{position:absolute;left:142px;top:30px;display:flex}
.footer-col{width:230px}
.footer-col h4{color:var(--white);font-size:12px;font-weight:700;margin-bottom:10px}
.footer-col p,.footer-col li{font-size:11px;line-height:20px;list-style:none}
.subscribe-input{width:170px;height:26px;background:var(--white);margin:10px 0;font-size:10px;color:#999;padding:6px 8px}
.subscribe-btn{width:94px;height:28px;background:var(--btn);color:var(--white);font-size:11px;font-weight:700;text-align:center;line-height:28px}
.social{display:flex;gap:8px;margin-bottom:22px}
.social span{width:20px;height:20px;background:#444;display:block}
.social span.on{background:#ffffff}
.trust{font-size:8px;color:#cccccc;font-weight:700;margin-bottom:8px}
.badges{display:flex;gap:5px}
.badges span{width:34px;height:20px;background:#dddddd;border-radius:2px;display:block}
.footer-bar{position:absolute;top:2180px;left:0;width:1200px;height:48px;background:var(--footer-bar);color:#888;font-size:11px;text-align:center;line-height:48px}
</style>
</head>
<body>

<header class="site-header">
  <div class="logo">alpenglow deals</div>
  <nav class="account-links"><span>My Account</span><span>My Wishlist</span><span>My Cart</span><span>Checkout</span><span>Log In</span></nav>
  <nav class="main-nav"><span>Home</span><span>Accommodation</span><span>Destinations</span><span>Vacation Places</span><span>Celebrate and Meet</span><span>Other Locations</span></nav>
</header>

<section class="hero" role="img" aria-label="Snowy alpine chalets under a blue winter sky with mountains behind">
  <div class="hero-arrow prev"><svg width="28" height="28"><path d="M16 8 L10 14 L16 20" stroke="#333" stroke-width="2.5" fill="none"/></svg></div>
  <div class="hero-arrow next"><svg width="28" height="28"><path d="M12 8 L18 14 L12 20" stroke="#333" stroke-width="2.5" fill="none"/></svg></div>
</section>

<form class="search-panel">
  <div class="search-row">
    <div class="field">Select City<span class="caret"></span></div>
    <div class="field">Check in</div>
    <div class="field">Check Out</div>
  </div>
  <div class="search-row">
    <div class="field">Bedrooms<span class="caret"></span></div>
    <div class="field">Price Range<span class="caret"></span></div>
    <div class="search-btn">SEARCH</div>
  </div>
</form>

<section class="section recent">
  <h2 class="section-title">Recently Added</h2>
  <div class="card-row">
    <article class="card">
      <div class="card-photo" role="img" aria-label="Hotel terrace with lounge chairs at dusk" style="background:linear-gradient(135deg,#8a6a4a,#c9a97a)"></div>
      <p class="card-name">Hotel Alba Crest at Summit Squa...</p>
      <p class="card-price">From : $1,000.00 - $1,500.00</p>
      <div class="card-actions"><span class="details-btn">CHECK DETAILS <svg width="12" height="12"><rect x="1" y="1" width="10" height="10" fill="none" stroke="#fff"/><path d="M4 6h4M6 4v4" stroke="#fff"/></svg></span><svg width="16" height="16"><path d="M2 7h3v8H2zM6 7l3-6c2 0 2 2 1.5 4H15v3l-2 7H6z" fill="#3478d1"/></svg></div>
      <hr>
    </article>
    <article class="card">
      <div class="card-photo" role="img" aria-label="Hotel room overlooking a city skyline" style="background:linear-gradient(135deg,#5d6f86,#c2c8cf)"></div>
      <p class="card-name">Hotel Alba Crest at Summit Squa...</p>
      <p class="card-price">From : $1,000.00 - $1,500.00</p>
      <div class="card-actions"><span class="details-btn">CHECK DETAILS <svg width="12" height="12"><rect x="1" y="1" width="10" height="10" fill="none" stroke="#fff"/><path d="M4 6h4M6 4v4" stroke="#fff"/></svg></span><svg width="16" height="16"><path d="M2 7h3v8H2zM6 7l3-6c2 0 2 2 1.5 4H15v3l-2 7H6z" fill="#3478d1"/></svg></div>
      <hr>
    </article>
    <article class="card">
      <div class="card-photo" role="img" aria-label="Warm hotel lounge interior" style="background:linear-gradient(135deg,#6b4a34,#b98c62)"></div>
      <p class="card-name">Hotel Alba Crest at Summit Squa...</p>
      <p class="card-price">From : $1,000.00 - $1,500.00</p>
      <div class="card-actions"><span class="details-btn">CHECK DETAILS <svg width="12" height="12"><rect x="1" y="1" width="10" height="10" fill="none" stroke="#fff"/><path d="M4 6h4M6 4v4" stroke="#fff"/></svg></span><svg width="16" height="16"><path d="M2 7h3v8H2zM6 7l3-6c2 0 2 2 1.5 4H15v3l-2 7H6z" fill="#3478d1"/></svg></div>
      <hr>
    </article>
  </div>
</section>

<section class="section luxury">
  <div class="family-photo" role="img" aria-label="Family with luggage ready for a holiday"></div>
  <h2 class="luxury-title">Luxury Hotel and Apartment For Family</h2>
  <div class="thumb-grid">
    <div class="thumb" role="img" aria-label="Hotel lobby" style="background:#4a3a30"><span class="thumb-label">CHECK DETAILS</span></div>
    <div class="thumb" role="img" aria-label="Hotel bedroom" style="background:#a88a6a"></div>
    <div class="thumb" role="img" aria-label="Dining room" style="background:#7d6a55"></div>
    <div class="thumb" role="img" aria-label="Apartment lounge" style="background:#b39a7a"></div>
    <div class="thumb" role="img" aria-label="Hotel suite" style="background:#8b7560"></div>
    <div class="thumb" role="img" aria-label="Restaurant interior" style="background:#5d4a3b"></div>
    <div class="thumb" role="img" aria-label="Bright bedroom" style="background:#c7b59c"></div>
    <div class="thumb" role="img" aria-label="Reception hall" style="background:#6e5a48"></div>
  </div>
</section>

<section class="section destinations">
  <h2 class="section-title">Top Destinations</h2>
  <div class="card-row">
    <article class="card">
      <div class="card-photo" role="img" aria-label="Grand hotel lobby with chandeliers" style="background:linear-gradient(135deg,#7a5a35,#d0a868)"></div>
      <p class="card-name">Hotel Alba Crest at Summit Squa...</p>
      <p class="card-price">From : $1,000.00 - $1,500.00</p>
      <div class="card-actions"><span class="details-btn">CHECK DETAILS <svg width="12" height="12"><rect x="1" y="1" width="10" height="10" fill="none" stroke="#fff"/><path d="M4 6h4M6 4v4" stroke="#fff"/></svg></span><svg width="16" height="16"><path d="M2 7h3v8H2zM6 7l3-6c2 0 2 2 1.5 4H15v3l-2 7H6z" fill="#3478d1"/></svg></div>
      <hr>
    </article>
    <article class="card">
      <div class="card-photo" role="img" aria-label="Resort pool under a blue sky" style="background:linear-gradient(180deg,#6fa7dc,#d9e3ea)"></div>
      <p class="card-name">Hotel Alba Crest at Summit Squa...</p>
      <p class="card-price">From : $1,000.00 - $1,500.00</p>
      <div class="card-actions"><span class="details-btn">CHECK DETAILS <svg width="12" height="12"><rect x="1" y="1" width="10" height="10" fill="none" stroke="#fff"/><path d="M4 6h4M6 4v4" stroke="#fff"/></svg></span><svg width="16" height="16"><path d="M2 7h3v8H2zM6 7l3-6c2 0 2 2 1.5 4H15v3l-2 7H6z" fill="#3478d1"/></svg></div>
      <hr>
    </article>
    <article class="card">
      <div class="card-photo" role="img" aria-label="Hotel dining hall" style="background:linear-gradient(135deg,#6a4b35,#c39a70)"></div>
      <p class="card-name">Hotel Alba Crest at Summit Squa...</p>
      <p class="card-price">From : $1,000.00 - $1,500.00</p>
      <div class="card-actions"><span class="details-btn">CHECK DETAILS <svg width="12" height="12"><rect x="1" y="1" width="10" height="10" fill="none" stroke="#fff"/><path d="M4 6h4M6 4v4" stroke="#fff"/></svg></span><svg width="16" height="16"><path d="M2 7h3v8H2zM6 7l3-6c2 0 2 2 1.5 4H15v3l-2 7H6z" fill="#3478d1"/></svg></div>
      <hr>
    </article>
  </div>
</section>

<footer class="site-footer">
  <div class="footer-cols">
    <div class="footer-col">
      <h4>SUBSCRIBE TODAY</h4>
      <p>Get the latest last minute ski deals</p>
      <p>hello@alpenglowdeals.com</p>
      <div class="subscribe-input">Enter your email</div>
      <div class="subscribe-btn">SUBSCRIBE</div>
    </div>
    <div class="footer-col">
      <h4>WELCOME</h4>
      <ul><li>Home</li><li>About Us</li><li>Article Authors</li><li>Testimonials</li><li>Contact Us</li></ul>
    </div>
    <div class="footer-col">
      <h4>INFORMATION</h4>
      <ul><li>Terms &amp; Conditions</li><li>Privacy Policy</li><li>Disclaimer</li><li>Sitemap</li></ul>
    </div>
    <div class="footer-col">
      <h4>FOLLOW US</h4>
      <p style="margin-bottom:10px">Connect with our social network</p>
      <div class="social"><span></span><span></span><span class="on"></span></div>
      <p class="trust">FAST DELIVERY | SECURE PAYMENT | 100% OFFICIAL</p>
      <div class="badges"><span></span><span></span><span></span><span></span><span></span></div>
    </div>
  </div>
</footer>
<div class="footer-bar">© 2015 AlpenGlowDeals.com. All Rights Reserved.</div>

</body>
</html>
```